Business card for a new cabinet shop company named Marlowe Cabinets for high end cabinets

Design a business card, thinking dark rich green with colours to speak of high end luxury ie; cream, gold, black possibly

Peter Lindqvar
Director Craftsman
Email: info@marlowecabinets.com.au
Instagram : @marlowe.cabinets

```html
<!DOCTYPE html>
<html lang="en">
<head>
<meta charset="utf-8">
<title>Marlowe Cabinets – Business Card</title>
<link rel="stylesheet" href="https://fonts.googleapis.com/css2?family=Montserrat:wght@400;500;700&display=swap">
<style>
  :root {
    --backdrop: #969696;
    --green: #1f3d2e;
    --green-sheen: #2c5441;
    --gold: #c9a65e;
    --gold-light: #dcc18a;
    --cream: #fbf7ee;
    --ink: #1f2a24;
  }
  * { margin: 0; padding: 0; box-sizing: border-box; }
  html, body {
    width: 1200px;
    height: 1108px;
    overflow: hidden;
    background: var(--backdrop);
    font-family: "Montserrat", sans-serif;
  }
  .canvas { position: relative; width: 1200px; height: 1108px; }

  .card {
    position: absolute;
    left: 242px;
    width: 716px;
    height: 409px;
    border-radius: 36px;
    overflow: hidden;
  }

  /* Front */
  .card-front {
    top: 119px;
    background: linear-gradient(115deg, var(--green) 0%, var(--green) 44%, var(--green-sheen) 55%, var(--green) 78%, var(--green) 100%);
  }
  .front-wordmark {
    position: absolute;
    left: 0; right: 0;
    top: 177px;
    text-align: center;
    font-weight: 500;
    font-size: 50px;
    letter-spacing: 1px;
    color: var(--gold-light);
  }

  /* Back */
  .card-back {
    top: 581px;
    background: var(--cream);
  }
  .back-wordmark {
    position: absolute;
    left: 40px;
    width: 300px;
    top: 187px;
    text-align: center;
    font-weight: 500;
    font-size: 27px;
    color: var(--green);
  }
  .divider {
    position: absolute;
    left: 356px;
    top: 81px;
    width: 2px;
    height: 247px;
    background: var(--gold);
  }
  .details {
    position: absolute;
    left: 380px;
    top: 78px;
    color: var(--ink);
  }
  .person-name {
    font-weight: 700;
    font-size: 31px;
    line-height: 36px;
    color: var(--gold);
  }
  .person-role {
    font-size: 18px;
    line-height: 24px;
    margin-top: 2px;
  }
  .address {
    font-size: 18px;
    line-height: 28px;
    margin-top: 14px;
  }
  .contacts {
    list-style: none;
    margin-top: 10px;
  }
  .contacts li {
    display: flex;
    align-items: center;
    font-size: 18px;
    line-height: 28.5px;
    white-space: nowrap;
  }
  .contacts svg {
    width: 15px;
    height: 15px;
    margin-right: 9px;
    flex: none;
    fill: var(--gold);
  }
</style>
</head>
<body>
<div class="canvas">

  <section class="card card-front">
    <div class="front-wordmark">Marlowe Cabinets</div>
  </section>

  <section class="card card-back">
    <div class="back-wordmark">Marlowe Cabinets</div>
    <div class="divider"></div>
    <div class="details">
      <h1 class="person-name">Peter Lindqvar</h1>
      <p class="person-role">Director Craftsman</p>
      <p class="address">Your address, City<br>State, Zip 1234</p>
      <ul class="contacts">
        <li>
          <svg viewBox="0 0 16 16" aria-hidden="true"><path d="M1 6c0-2 3-3 7-3s7 1 7 3v1h-3V5.5C11 5 9.5 5 8 5S5 5 4 5.5V7H1z"/><path d="M3 8h10l1 6H2z"/></svg>
          123 456 789
        </li>
        <li>
          <svg viewBox="0 0 16 16" aria-hidden="true"><path d="M1 3h14v10H1z"/><path d="M2 4.5l6 4.5 6-4.5" fill="none" stroke="#fbf7ee" stroke-width="1.2"/></svg>
          info@marlowecabinets.com.au
        </li>
        <li>
          <svg viewBox="0 0 16 16" aria-hidden="true"><circle cx="8" cy="8" r="6.5"/></svg>
          @marlowe.cabinets
        </li>
        <li>
          <svg viewBox="0 0 16 16" aria-hidden="true"><circle cx="8" cy="8" r="7"/><path d="M4 4c2 1 1 3 3 3s1 3 2 4l-2 3c-3-1-4-4-3-5s-2-2 0-5zM10 2c0 2 2 2 3 3-1 1-3 0-3-3z" fill="#fbf7ee"/></svg>
          www.marlowecabinets.com.au
        </li>
      </ul>
    </div>
  </section>

</div>
</body>
</html>
```